Professional & attention grabbing.

A business card design, front and back. I already have a logo I will attach, but I am open to something new as well.
Things to include:
Name:
Title:
Phone:
Email:
Wanting something that is professional but attention grabbing.
Also we do a lot of work using drones on natural gas pipelines (leading the future)if you want to include any of that. I'm open to ideas.
Target Market(s)
Natural gas transmission industry / greenhouse gas mitigation industry
Industry/Entity Type
Business
Contact Information for Business Card
All details have been conveyed above.
Colors
Designer to choose colors to be used in the design.
Look and feel
Each slider illustrates characteristics of the customer's brand and the style your logo design should communicate.

```html
<!DOCTYPE html>
<html lang="en">
<head>
<meta charset="utf-8">
<title>Kestrel Inspections — Business Card</title>
<link rel="stylesheet" href="https://fonts.googleapis.com/css2?family=Roboto+Condensed:wght@400;700&display=swap">
<style>
  :root {
    --brand-red: #c11f27;
    --slate: #3f4043;
    --paper: #ffffff;
    --backdrop: #e9e6e1;
    --ink-light: #ffffff;
  }
  * { box-sizing: border-box; margin: 0; padding: 0; }
  html, body {
    width: 1200px; height: 900px; overflow: hidden;
    background: var(--backdrop);
    font-family: "Roboto Condensed", Arial, sans-serif;
  }
  .stage { position: relative; width: 1200px; height: 900px; }

  .card {
    position: absolute;
    box-shadow: 0 10px 28px rgba(0,0,0,.18);
    overflow: hidden;
  }

  /* ---------- Contact side (portrait) ---------- */
  .card-contact {
    left: 130px; top: 170px; width: 320px; height: 560px;
    background: var(--paper);
  }
  .edge-stripe {
    position: absolute; top: 0; bottom: 0; width: 12px; background: var(--brand-red);
  }
  .edge-stripe.left { left: 0; }
  .edge-stripe.right { right: 0; }
  .corner-wedge {
    position: absolute; top: 0; left: 170px; width: 150px; height: 22px;
    background: var(--brand-red);
  }

  .contact-brand {
    position: absolute; top: 52px; right: 34px;
    display: flex; align-items: center; gap: 10px;
  }
  .brand-square { width: 34px; height: 34px; background: var(--brand-red); }
  .brand-name {
    font-weight: 700; font-size: 30px; line-height: 1; color: var(--slate);
    letter-spacing: .5px;
  }

  .company-band {
    position: absolute; top: 150px; left: 64px; right: 12px; height: 56px;
    background: var(--slate); color: var(--ink-light);
    display: flex; align-items: center; padding-left: 20px;
    font-size: 20px; letter-spacing: .5px;
  }

  .contact-row {
    position: absolute; left: 12px; right: 12px; height: 52px;
    display: flex; align-items: flex-start;
  }
  .contact-row .rule {
    position: absolute; left: 0; top: 0; width: 64px; height: 8px; background: var(--brand-red);
  }
  .contact-row .icon {
    position: relative; margin-left: 26px; width: 38px; height: 38px;
    background: var(--brand-red);
    display: flex; align-items: center; justify-content: center;
  }
  .contact-row .icon svg { width: 20px; height: 20px; fill: var(--ink-light); }
  .contact-row .value {
    margin-left: 12px; margin-top: 30px; flex: 1;
    background: var(--slate); color: var(--ink-light);
    padding: 10px 14px; font-size: 16px; line-height: 1.15;
  }
  .row-phone { top: 238px; }
  .row-phone .value { font-size: 22px; }
  .row-email { top: 338px; }
  .row-email .value { font-size: 14px; letter-spacing: .2px; }
  .row-sector { top: 430px; }

  .foot-band {
    position: absolute; left: 0; right: 0; bottom: 0; height: 14px; background: var(--brand-red);
  }

  /* ---------- Brand side (landscape) ---------- */
  .card-brand {
    left: 520px; top: 290px; width: 560px; height: 320px;
    background: var(--brand-red);
    display: flex; align-items: center; justify-content: center;
  }
  .brand-lockup { display: flex; align-items: center; gap: 22px; }
  .brand-lockup .mark { width: 70px; height: 70px; background: var(--ink-light); }
  .brand-lockup .wordmark {
    color: var(--ink-light); font-weight: 700; font-size: 58px; line-height: .95;
    letter-spacing: 1px;
  }
</style>
</head>
<body>
<main class="stage">

  <section class="card card-contact" aria-label="Business card, contact side">
    <div class="edge-stripe left"></div>
    <div class="edge-stripe right"></div>
    <div class="corner-wedge"></div>

    <div class="contact-brand">
      <span class="brand-square"></span>
      <span class="brand-name">KESTREL</span>
    </div>

    <div class="company-band">KESTREL INSPECTIONS</div>

    <div class="contact-row row-phone">
      <span class="rule"></span>
      <span class="icon">
        <svg viewBox="0 0 24 24" aria-hidden="true"><path d="M6.6 10.8a15.1 15.1 0 0 0 6.6 6.6l2.2-2.2c.3-.3.7-.4 1-.2 1.1.4 2.3.6 3.6.6.6 0 1 .4 1 1V20c0 .6-.4 1-1 1A17 17 0 0 1 3 4c0-.6.4-1 1-1h3.5c.6 0 1 .4 1 1 0 1.3.2 2.5.6 3.6.1.3 0 .7-.2 1z"/></svg>
      </span>
      <span class="value">555 0142 0199</span>
    </div>

    <div class="contact-row row-email">
      <span class="rule"></span>
      <span class="icon">
        <svg viewBox="0 0 24 24" aria-hidden="true"><path d="M3 5h18v14H3z M3 5l9 7 9-7" fill="none" stroke="#fff" stroke-width="2" stroke-linejoin="round"/></svg>
      </span>
      <span class="value">OFFICE@KESTRELINSPECT.COM</span>
    </div>

    <div class="contact-row row-sector">
      <span class="rule"></span>
      <span class="icon">
        <svg viewBox="0 0 24 24" aria-hidden="true"><path d="M12 2a7 7 0 0 0-7 7c0 5.2 7 13 7 13s7-7.8 7-13a7 7 0 0 0-7-7zm0 9.5A2.5 2.5 0 1 1 12 6.5a2.5 2.5 0 0 1 0 5z"/></svg>
      </span>
      <span class="value">Natural gas<br>transmission industry</span>
    </div>

    <div class="foot-band"></div>
  </section>

  <section class="card card-brand" aria-label="Business card, brand side">
    <div class="brand-lockup">
      <span class="mark"></span>
      <span class="wordmark">KESTREL<br>INSPECTIONS</span>
    </div>
  </section>

</main>
</body>
</html>
```